Business Card Design

I need a business card design for a new company based in Sydney called 'The Copper Ladle'. We deliver organic, gourmet and fine foods to your door.

I would like to see creative, unique designs which use colours which represent health and nature like green.

Target Market(s)

Health conscious 20 to 35 year olds.

Industry/Entity Type

Health

Contact Information for Business Card

The Copper Ladle, Owen Barclett, owen@thecopperladle.com.au, 0427685392

Requirements
Must have
• My logo.

```html
<!DOCTYPE html>
<html lang="en">
<head>
<meta charset="utf-8">
<title>The Copper Ladle – Business Card</title>
<link href="https://fonts.googleapis.com/css2?family=Open+Sans:wght@300;400;700&display=swap" rel="stylesheet">
<style>
  :root {
    --backdrop: #dcdde0;
    --card: #ffffff;
    --leaf-green: #7cb518;
    --deep-green: #3f8a2c;
    --text-grey: #55585c;
    --rule-grey: #cfd1d4;
  }
  * { box-sizing: border-box; margin: 0; padding: 0; }
  html, body {
    width: 1200px; height: 800px; overflow: hidden;
    background: var(--backdrop);
    font-family: "Open Sans", Arial, sans-serif;
  }
  .canvas {
    width: 1200px; height: 800px;
    display: flex; align-items: center; justify-content: center; gap: 40px;
  }
  .card {
    position: relative;
    width: 540px; height: 310px;
    background: var(--card);
    box-shadow: 0 2px 6px rgba(0,0,0,0.12);
  }
  /* Front */
  .card--front {
    display: flex; flex-direction: column; align-items: center; justify-content: center;
  }
  .brand {
    display: flex; align-items: center; gap: 12px;
  }
  .brand__dot {
    width: 34px; height: 34px; border-radius: 50%;
    background: var(--leaf-green);
  }
  .brand__name {
    font-weight: 300; font-size: 32px; line-height: 1;
    color: var(--deep-green);
  }
  .card--front .website {
    margin-top: 34px;
    font-size: 13px; color: var(--text-grey);
  }
  /* Back */
  .card--back .holder {
    position: absolute; left: 40px; top: 62px;
    font-weight: 700; font-size: 14px; color: var(--leaf-green);
  }
  .card--back .rule {
    position: absolute; left: 36px; height: 1px; background: var(--rule-grey);
  }
  .rule--top { top: 92px; width: 250px; }
  .rule--bottom { top: 228px; right: 36px; }
  .card--back .brand {
    position: absolute; right: 36px; top: 56px;
  }
  .card--back .brand__name { font-size: 26px; }
  .card--back .brand__dot { width: 28px; height: 28px; }
  .contacts {
    position: absolute; left: 36px; right: 36px; top: 140px;
    display: flex; justify-content: space-between; list-style: none;
  }
  .contact {
    display: flex; flex-direction: column; align-items: center; gap: 6px;
    font-size: 12px; color: var(--text-grey);
  }
  .contact svg { width: 12px; height: 12px; fill: none; stroke: var(--leaf-green); stroke-width: 1.6; }
</style>
</head>
<body>
<main class="canvas">
  <section class="card card--front">
    <div class="brand">
      <span class="brand__dot"></span>
      <span class="brand__name">The Copper Ladle</span>
    </div>
    <p class="website">www.thecopperladle.com.au</p>
  </section>

  <section class="card card--back">
    <p class="holder">Owen Barclett</p>
    <div class="rule rule--top"></div>
    <div class="brand">
      <span class="brand__dot"></span>
      <span class="brand__name">The Copper Ladle</span>
    </div>
    <ul class="contacts">
      <li class="contact">
        <svg viewBox="0 0 12 12"><rect x="1" y="2.5" width="10" height="7"/><path d="M1 2.5l5 4 5-4"/></svg>
        <span>owen@thecopperladle.com.au</span>
      </li>
      <li class="contact">
        <svg viewBox="0 0 12 12"><rect x="3" y="1" width="6" height="10" rx="1"/><path d="M5.5 9.2h1"/></svg>
        <span>0427685392</span>
      </li>
      <li class="contact">
        <svg viewBox="0 0 12 12"><circle cx="6" cy="6" r="5"/><path d="M1 6h10M6 1c-2.5 3-2.5 7 0 10M6 1c2.5 3 2.5 7 0 10"/></svg>
        <span>www.thecopperladle.com.au</span>
      </li>
    </ul>
    <div class="rule rule--bottom"></div>
  </section>
</main>
</body>
</html>
```